Following list to be designed:

1. A4 Letter Head

Must comprise of:
BRISK HARBOR and its LOGO
Address: No.41, 2F, Telvin Court, Marlow Lane, Upper Fennel Gardens, Bangalore 560 078
Tel: 080 41927380
Fax: 080 41927381
Mail: hello@briskharbor.example

Color of wordings to be in the lighter shade of blue and brighter shade of blue.

2. A4 Envelope

Must comprise of:
BRISK HARBOR and its LOGO
Tel: 080 41927380
Fax: 080 41927381

3. Postal Envelope

Must comprise of:
BRISK HARBOR and its LOGO
Tel: 080 41927380
Fax: 080 41927381

4. Business Card

Must comprise of:
Ravi Menon
Managing Partner
Cell: +91 9847162053
Mail: ravimenon@briskharbor.example
Tel: 080 41927380
Fax: 080 41927381

5. A4 Letter Head

Must comprise of:
BRISK HARBOR CORP. (wording) and BRISK HARBOR LOGO (only blue ribbon)

Blue ribbon (BRISK HARBOR LOGO) may be placed on Left Top Corner of the A4 Letter Head
and BRISK HARBOR CORP. (wording) to be placed on Right Top Corner of the A4 Letter Head

Tel: 080 41927380
Fax: 080 41927381

6. . A4 Envelope

Must comprise of:

Blue ribbon (BRISK HARBOR LOGO) may be placed on Left Top Corner of the A4 Envelope
and BRISK HARBOR CORP. (wording) to be placed on Right Top Corner of the A4 Envelope
Tel: 080 41927380
Fax: 080 41927381

Target Market(s)

Top IT/ITES Organizations

Industry/Entity Type

Real Estate Development

Font styles to use
Serif
Sans Serif

Colors
33a6d7
0792cd
85cae6

Requirements
Should not have
• Playful font and color

```html
<!DOCTYPE html>
<html lang="en">
<head>
<meta charset="utf-8">
<title>Brisk Harbor – Business Card</title>
<link rel="stylesheet" href="https://fonts.googleapis.com/css2?family=Open+Sans:wght@400;600;700&display=swap">
<style>
  :root {
    --page-bg: #eceeee;
    --card-white: #ffffff;
    --brand-blue: #2f6aa8;
    --brand-bright: #33a6d7;
    --brand-light: #85cae6;
    --back-edge: #3f6e9f;
    --back-center: #56a6d2;
    --text-dark: #2b2b2b;
    --text-muted: #6b6a5e;
    --rule: #b9b6ad;
  }
  * { box-sizing: border-box; margin: 0; padding: 0; }
  html, body {
    width: 1200px; height: 1061px; overflow: hidden;
    background: var(--page-bg);
    font-family: "Open Sans", sans-serif;
  }
  .sheet { position: relative; width: 1200px; height: 1061px; }
  .card {
    position: absolute; left: 190px; width: 820px; height: 469px;
    box-shadow: 0 4px 14px rgba(0,0,0,.12);
  }
  .card-front { top: 40px; background: var(--card-white); }
  .card-back {
    top: 552px;
    background: radial-gradient(circle at 50% 48%, var(--back-center) 0%, #4b8cc0 40%, var(--back-edge) 85%);
    display: flex; align-items: center; justify-content: center;
  }
  .brand {
    position: absolute; left: 70px; top: 190px; width: 300px;
    display: flex; align-items: center; gap: 14px;
  }
  .brand-mark { width: 22px; height: 22px; background: var(--brand-blue); flex: none; }
  .brand-name {
    font-weight: 700; font-size: 31px; letter-spacing: 1px;
    color: var(--brand-blue); white-space: nowrap;
  }
  .divider {
    position: absolute; left: 400px; top: 60px; width: 1px; height: 350px;
    background: var(--rule);
  }
  .details { position: absolute; left: 432px; top: 62px; right: 30px; }
  .person-name { font-size: 33px; font-weight: 700; color: var(--brand-blue); line-height: 1.1; }
  .person-title { font-size: 18px; color: var(--text-muted); margin-top: 2px; }
  .address {
    font-size: 17px; color: var(--text-dark); line-height: 1.45;
    margin-top: 30px; font-style: normal;
  }
  .contact-list { list-style: none; margin-top: 22px; }
  .contact-item {
    display: flex; align-items: center; gap: 14px;
    font-size: 17px; color: var(--text-dark); height: 32px;
  }
  .contact-icon { width: 24px; height: 24px; flex: none; }
  .back-name {
    color: #ffffff; font-weight: 600; font-size: 38px; letter-spacing: 3px;
  }
</style>
</head>
<body>
<main class="sheet">
  <section class="card card-front">
    <div class="brand">
      <span class="brand-mark"></span>
      <span class="brand-name">BRISK HARBOR</span>
    </div>
    <div class="divider"></div>
    <div class="details">
      <h1 class="person-name">Ravi Menon</h1>
      <p class="person-title">Managing Partner</p>
      <address class="address">No.41, 2F, Telvin Court, Marlow Lane,<br>Upper Fennel Gardens,<br>Bangalore 560 078</address>
      <ul class="contact-list">
        <li class="contact-item">
          <svg class="contact-icon" viewBox="0 0 24 24"><rect width="24" height="24" rx="2" fill="var(--brand-blue)"/><rect x="8" y="4" width="8" height="16" rx="1.5" fill="none" stroke="#fff" stroke-width="1.6"/><circle cx="12" cy="17.5" r="0.9" fill="#fff"/></svg>
          <span>+91 9847162053</span>
        </li>
        <li class="contact-item">
          <svg class="contact-icon" viewBox="0 0 24 24"><rect width="24" height="24" rx="2" fill="var(--brand-blue)"/><path d="M7 6c0 6 5 11 11 11l1-3-3-1-1.5 1.5c-1.8-.9-3.2-2.3-4-4L12 9l-1-3z" fill="#fff"/></svg>
          <span>080 41927380</span>
        </li>
        <li class="contact-item">
          <svg class="contact-icon" viewBox="0 0 24 24"><rect width="24" height="24" rx="2" fill="var(--brand-blue)"/><rect x="8" y="4" width="8" height="5" fill="#fff"/><rect x="5" y="9" width="14" height="7" rx="1" fill="#fff"/><rect x="8" y="14" width="8" height="6" fill="#fff" stroke="var(--brand-blue)" stroke-width="1"/></svg>
          <span>080 41927381</span>
        </li>
        <li class="contact-item">
          <svg class="contact-icon" viewBox="0 0 24 24"><rect width="24" height="24" rx="2" fill="var(--brand-blue)"/><rect x="5" y="7" width="14" height="10" fill="#fff"/><path d="M5 7l7 6 7-6" fill="none" stroke="var(--brand-blue)" stroke-width="1.3"/></svg>
          <span>ravimenon@briskharbor.example</span>
        </li>
      </ul>
    </div>
  </section>

  <section class="card card-back">
    <span class="back-name">BRISK HARBOR</span>
  </section>
</main>
</body>
</html>
```